Eine Willkommenseite (Startseite) für WohnFokus
Zielgruppe
Die Zielgruppe sind Kunden (Business, Privat und öffentliche Einrichtungen) die Immobilien über das Wohnfokus-Portal kostenlos suchen oder inserieren möchten. Quasi alle Besucher, die Immobilen über WohnFokus ohne Inseratkosten verkaufen, kaufen, vermieten, mieten und versteigern wollen.
Aufgabenstellung
Die Willkommenseite für WohnFokus.
Problemstellung: WohnFokus ist seit ca. 3 Monaten erfolgreich online. Die Immobilen Webseite von WohnFokus ist schlicht, dezent sowie funktionell aufgebaut. WohnFokus fehlt eine ansprechende Willkommenseite. Die Willkommenseite sollte emotional ansprechend und dem/der BesucherIn ein "Wow" entlocken sowie zu einem weiteren Surfen auf WohnFokus einladen.

```html
<!DOCTYPE html>
<html lang="de">
<head>
<meta charset="utf-8">
<title>WohnFokus – Willkommen</title>
<link rel="stylesheet" href="https://fonts.googleapis.com/css2?family=Arimo:ital,wght@0,400;0,700;1,700&display=swap">
<style>
  :root {
    --band-blue: #7d9ccf;
    --brand-blue: #1f74b8;
    --ink: #1c1c1c;
    --ink-soft: #333;
    --card-border: #b9cbe0;
    --side-bg: #eef0f3;
    --search-border: #b8c2d0;
    --search-text: #c3c8cf;
    --go-bg: #141a55;
    --icon-grey: #8f98a6;
  }
  * { box-sizing: border-box; margin: 0; padding: 0; }
  html, body {
    width: 1200px; height: 854px; overflow: hidden;
    font-family: "Arimo", Arial, sans-serif;
    color: var(--ink);
    background: linear-gradient(180deg, #f7f7f7 0%, #e9e9e9 35%, #ffffff 60%, #efefef 100%);
  }
  .page {
    position: absolute; left: 175px; top: 3px;
    width: 898px; height: 848px;
    background: #fff;
    border-left: 1px solid #c9d3e2;
    border-right: 1px solid #c9d3e2;
    overflow: hidden;
  }
  .band { position: absolute; left: 0; width: 100%; height: 19px; background: var(--band-blue); }
  .band--top { top: 0; }
  .band--bottom { bottom: 0; }

  .hero-photo {
    position: absolute; left: 299px; top: 19px; width: 404px; height: 810px;
    background: linear-gradient(90deg, #ffffff 0%, #e4e6ea 16%, #c6cbd4 40%, #b6bcc7 50%, #3b3935 52%, #2e2c2a 75%, #3a3a3a 100%);
  }
  .side-column {
    position: absolute; left: 703px; top: 19px; width: 195px; height: 810px;
    background: linear-gradient(90deg, #e6e8ec 0%, var(--side-bg) 40%, #f7f8fa 100%);
  }

  .brand {
    position: absolute; left: 40px; top: 118px;
    display: flex; align-items: center; gap: 10px;
  }
  .brand__mark { width: 22px; height: 22px; background: var(--brand-blue); }
  .brand__name { font-size: 29px; font-weight: 700; color: var(--brand-blue); letter-spacing: 0.5px; }

  .welcome {
    position: absolute; left: 39px; top: 198px;
    font-size: 21px; letter-spacing: 11.5px; color: var(--ink-soft);
  }
  .intro {
    position: absolute; left: 39px; top: 242px; width: 233px;
    font-size: 15px; line-height: 18.7px; text-align: justify; color: var(--ink);
  }

  .cta {
    position: absolute; left: 37px; top: 698px;
    font-size: 20px; font-weight: 700; font-style: italic; color: var(--brand-blue);
  }
  .search {
    position: absolute; left: 40px; top: 728px; width: 200px; height: 24px;
    display: flex; border: 1px solid var(--search-border); border-radius: 3px; background: #fff;
  }
  .search__field {
    flex: 1; padding-left: 8px; line-height: 22px;
    font-size: 15px; font-style: italic; color: var(--search-text); white-space: nowrap; overflow: hidden;
  }
  .search__go {
    width: 34px; background: var(--go-bg); color: #fff;
    font-size: 15px; font-weight: 700; font-style: italic; text-align: center; line-height: 22px;
  }

  .footer-nav {
    position: absolute; left: 43px; top: 810px;
    display: flex; gap: 26px; font-size: 13px; color: var(--ink);
  }
  .social {
    position: absolute; left: 748px; top: 807px; display: flex; gap: 7px;
  }
  .social span { width: 14px; height: 14px; background: var(--icon-grey); border-radius: 2px; }

  .listing {
    position: absolute; left: 726px; width: 151px; height: 131px;
    background: #fff; border: 1px solid var(--card-border);
  }
  .listing__photo { position: absolute; left: 8px; top: 10px; width: 133px; height: 85px; }
  .listing__caption {
    position: absolute; left: 0; right: 0; bottom: 8px;
    text-align: center; font-size: 14px; color: var(--ink);
  }
  .listing:nth-of-type(1) { top: 56px; }
  .listing:nth-of-type(2) { top: 200px; }
  .listing:nth-of-type(3) { top: 344px; }
  .listing:nth-of-type(4) { top: 487px; }
  .listing:nth-of-type(5) { top: 632px; }
  .photo-house-red { background: linear-gradient(180deg, #c9dcee 0%, #d9dde0 40%, #b9556a 55%, #5d8a3c 85%, #4c7a2c 100%); }
  .photo-bedroom { background: linear-gradient(180deg, #e7e7e5 0%, #cfd2d3 40%, #7b7a78 70%, #5a5552 100%); }
  .photo-townhouse { background: linear-gradient(180deg, #8fb0cf 0%, #a66060 35%, #6d4c45 65%, #6e8f45 100%); }
  .photo-office { background: linear-gradient(180deg, #dcdcd8 0%, #c2c2bc 40%, #5d5a55 65%, #8a8680 100%); }
  .photo-villa { background: linear-gradient(180deg, #2f6fb5 0%, #7aa7d8 35%, #ececec 55%, #6c9a3d 85%, #4a7a26 100%); }
</style>
</head>
<body>
<main class="page">
  <div class="band band--top"></div>

  <div class="hero-photo" role="img" aria-label="Nahaufnahme einer geöffneten Haustür mit Schlüssel im Schloss"></div>
  <aside class="side-column"></aside>

  <div class="brand">
    <span class="brand__mark"></span>
    <span class="brand__name">WohnFokus</span>
  </div>

  <h1 class="welcome">Willkommen</h1>
  <p class="intro">auf der Seite von Wohnfokus. Lorem ipsum dolor sit amet, consetetur sadipscing elitr, sed diam nonumy eirmod tempor invidunt ut labore et dolore magna aliquyam erat, sed diam voluptua. At vero eos et accusam et justo duo dolores et ea rebum. Stet clita kasd gubergren, no sea takimata sanctus est Lorem ipsum dolor sit amet. Lorem ipsum dolor sit amet, consetetur sadipscing elitr, sed diam nonumy eirmod tempor invidunt ut labore et dolore magna aliquyam erat, sed diam voluptua. At vero eos et accusam et justo duo dolores et ea rebum. Stet clita kasd gubergren, no sea takimata sanctus est Lorem ipsum dolor sit amet.</p>

  <p class="cta">Ich will teilnehmen!</p>
  <div class="search">
    <span class="search__field">SOFORT SUCHE ...</span>
    <span class="search__go">GO</span>
  </div>

  <nav class="footer-nav">
    <span>AGB</span>
    <span>IMPRESSUM/KONTAKT</span>
    <span>KOOPERARTIONSPARTNER</span>
  </nav>
  <div class="social" aria-label="Soziale Netzwerke">
    <span></span><span></span><span></span><span></span><span></span>
  </div>

  <section class="listings">
    <article class="listing">
      <div class="listing__photo photo-house-red" role="img" aria-label="Modernes Einfamilienhaus mit roter Fassade im Garten"></div>
      <p class="listing__caption">Lorem ipsum dolo</p>
    </article>
    <article class="listing">
      <div class="listing__photo photo-bedroom" role="img" aria-label="Helles Schlafzimmer mit großem Fenster"></div>
      <p class="listing__caption">Lorem ipsum dolo</p>
    </article>
    <article class="listing">
      <div class="listing__photo photo-townhouse" role="img" aria-label="Mehrstöckiges Stadthaus mit roter Fassade"></div>
      <p class="listing__caption">Lorem ipsum dolo</p>
    </article>
    <article class="listing">
      <div class="listing__photo photo-office" role="img" aria-label="Heller Besprechungsraum mit Bücherregal"></div>
      <p class="listing__caption">Lorem ipsum dolo</p>
    </article>
    <article class="listing">
      <div class="listing__photo photo-villa" role="img" aria-label="Weiße Villa mit Garten unter blauem Himmel"></div>
      <p class="listing__caption">Lorem ipsum dolo</p>
    </article>
  </section>

  <div class="band band--bottom"></div>
</main>
</body>
</html>
```